Fernlee Shopping Centre main sign re-design project

We would like to refresh the look of the main sign we have on the corner of a block of shops to make it more contemproary and vibrant.

A picture of the existing sign which reads Fernlee Shopping Centre can be found in attached PDF and at the following URL.

http://www.quornvale-example.co.nz/~/media/Listings/Region%20One/Town%20Centre/Central%20District/481297/Images/481297_1.ashx?bc=Gainsboro&as=1&h=550&w=980&ma=1

Fernlee Shopping Centre is also know locally as Fernlee Plaza, but the key word is Fernlee.

The existing signage has a flower/clover pattern on it which I think was just added to create a bit of interest. The building is located in a town surrounded by farm land.

I do quite like the organic feel of plant leaves or certain flowers - preferably New Zealand native plants for instance - the Kowhai flower or leaf block, pohutukawa, or kaka beak - reference images can be found with google image search

Geometric patterns could also be an option.

Once again the imagery is only to soften the sign and add some interest.
Updates

Target Market(s)

The target audience is premium shopper

Industry/Entity Type

Building

Requirements
Must have
• Must have the words: Fernlee Shopping Centre.
The big M is not essential, and I would rather the emphasis was on the word Fernlee.
Should not have
• Should not be brown. We want the sign to feel more contemporary, but not too hard. The current pale brown feels too soft in comparison with the look of the building.

```html
<!DOCTYPE html>
<html lang="en">
<head>
<meta charset="utf-8">
<title>Fernlee Shopping Centre – Sign Panels</title>
<link href="https://fonts.googleapis.com/css2?family=Exo+2:wght@700;800&display=swap" rel="stylesheet">
<style>
  :root {
    --lime: #b9f23f;
    --lime-deep: #8fbc2b;
    --disc: #d9dcd6;
    --disc-rim: #9aa096;
    --ink: #111111;
    --paper: #ffffff;
    --sheet: #ffffff;
  }
  * { margin: 0; padding: 0; box-sizing: border-box; }
  html, body {
    width: 1200px;
    height: 1000px;
    overflow: hidden;
    background: var(--sheet);
  }
  .sign-set {
    position: relative;
    width: 1200px;
    height: 1000px;
    display: flex;
    justify-content: center;
    align-items: center;
    gap: 50px;
  }
  .sign-panel {
    position: relative;
    width: 300px;
    height: 600px;
    background: var(--lime);
    overflow: hidden;
    font-family: "Exo 2", "Arial Black", sans-serif;
  }
  .sign-panel__band {
    position: absolute;
    inset: 0;
    width: 300px;
    height: 600px;
  }
  .sign-panel__band path { fill: var(--lime-deep); }
  .sign-panel__decor {
    position: absolute;
    pointer-events: none;
  }
  .decor--leaves {
    left: 10px; top: 250px; width: 220px; height: 170px;
    background: radial-gradient(ellipse at 50% 55%, rgba(120,190,50,0.75) 0%, rgba(150,210,70,0.35) 55%, rgba(185,242,63,0) 75%);
  }
  .decor--flourish {
    left: 20px; top: 190px; width: 280px; height: 410px;
    background: radial-gradient(ellipse at 65% 55%, rgba(255,255,255,0.35) 0%, rgba(255,255,255,0.12) 50%, rgba(255,255,255,0) 75%);
  }
  .decor--rings {
    left: 0; top: 200px; width: 300px; height: 400px;
    background: radial-gradient(ellipse at 60% 70%, rgba(255,255,255,0.28) 0%, rgba(255,255,255,0.1) 50%, rgba(255,255,255,0) 75%);
  }
  .decor--sprig {
    left: 20px; top: 0; width: 140px; height: 110px;
    background: radial-gradient(ellipse at 40% 40%, rgba(255,255,255,0.4) 0%, rgba(255,255,255,0) 70%);
  }
  .sign-panel__disc {
    position: absolute;
    left: 50px; top: 55px;
    width: 200px; height: 200px;
    border-radius: 50%;
    background: var(--disc);
    border: 5px solid var(--disc-rim);
  }
  .sign-panel__name {
    position: absolute;
    left: 0; right: 0;
    top: 268px;
    text-align: center;
    font-weight: 800;
    font-size: 56px;
    line-height: 1;
    color: var(--ink);
    letter-spacing: -0.5px;
  }
  .sign-panel__tagline {
    position: absolute;
    left: 0; right: 0;
    top: 455px;
    text-align: center;
    font-weight: 700;
    font-size: 40px;
    line-height: 1.3;
    color: var(--ink);
  }
  .sign-panel--leaf .sign-panel__tagline { color: var(--paper); }
</style>
</head>
<body>
<main class="sign-set">

  <section class="sign-panel sign-panel--leaf">
    <svg class="sign-panel__band" viewBox="0 0 300 600" aria-hidden="true">
      <path d="M0 425 C 90 395, 200 330, 300 270 L300 600 L0 600 Z"/>
    </svg>
    <div class="sign-panel__decor decor--leaves" role="img" aria-label="Cluster of fresh green leaves"></div>
    <div class="sign-panel__disc"></div>
    <h2 class="sign-panel__name">Fernlee</h2>
    <p class="sign-panel__tagline">Shopping<br>centre</p>
  </section>

  <section class="sign-panel sign-panel--flourish">
    <svg class="sign-panel__band" viewBox="0 0 300 600" aria-hidden="true">
      <path d="M0 445 C 100 415, 210 355, 300 315 L300 600 L0 600 Z"/>
    </svg>
    <div class="sign-panel__decor decor--flourish" role="img" aria-label="White floral flourish sweeping up the panel"></div>
    <div class="sign-panel__disc"></div>
    <h2 class="sign-panel__name">Fernlee</h2>
    <p class="sign-panel__tagline">Shopping<br>centre</p>
  </section>

  <section class="sign-panel sign-panel--rings">
    <svg class="sign-panel__band" viewBox="0 0 300 600" aria-hidden="true">
      <path d="M0 455 C 100 420, 210 345, 300 295 L300 600 L0 600 Z"/>
    </svg>
    <div class="sign-panel__decor decor--sprig" role="img" aria-label="Small white floral sprig"></div>
    <div class="sign-panel__decor decor--rings" role="img" aria-label="Pattern of white concentric rings"></div>
    <div class="sign-panel__disc"></div>
    <h2 class="sign-panel__name">Fernlee</h2>
    <p class="sign-panel__tagline">Shopping<br>centre</p>
  </section>

</main>
</body>
</html>
```